Termite Rack Card 4 x 9 or 3.5 x 8.5

You will see an older version of the HarborTermiteRack Card this will need to be modernized with the look and branding feel of the 2024HarborFlyer file that is attached.

Remove the following verbiage from the older version- FREE TERMITE INSPECTIONS- BEST PRICES SHOULD BE REPLACED WITH COMPETITIVE PRICES- Remove paragraph our 50 Certified Master inspectors and Our Harbor Group Termite Division provides Free... Remove we will beat any fumigation or legtimate repair.

The following verbiage on one side.

Protect your Client's greatest asset with a Pre-Listing Termite Inspection

Speed up the Sales Process - By having the seller conduct a termite inspection, you reduce the risk of delays or complications. With this essential step complete, you can expedite the transaction timeline and close deals faster!

Enhance Property Value - Uncovering and remedying termite problems early can prevent costly damages and preserve the integrity of the home. With a clean bill of health from a termite inspection, you can market the property with confidence!

Boost Buyer Confidence - A pre-listing termite inspection demonstrates proactive care for the property, instilling trust in potential buyers. Identifying issues upfront, you also eliminate surprises during negotiations, leading to smoother transactions and happier clients.

The Following Bullet points on the opposite side-
HARBOR GROUP
TERMITE SOLUTIONS

*Pre-Listing Inspections
*Inspection
*Treatment
*Repairs
*Fumigations
*Bill Repairs through Escrow
*Over 40 Years Experience
*Modern and effective treatmetns
*Quality and Integrity

```html
<!DOCTYPE html>
<html lang="en">
<head>
<meta charset="UTF-8">
<title>Harbor Group – Pre-Listing Termite Inspection Rack Card</title>
<link href="https://fonts.googleapis.com/css2?family=Open+Sans:wght@400;600;700;800&display=swap" rel="stylesheet">
<style>
  :root{
    --brand-blue:#0f66b8;
    --ink-grey:#5c6168;
    --stage:#d9dadc;
    --paper:#ffffff;
    --paper-shade:#e4e6e9;
    --ribbon-red:#e3161d;
    --footer-black:#0c0e12;
    --sky-light:#d5e4f5;
  }
  *{box-sizing:border-box;margin:0;padding:0}
  html,body{width:1200px;height:802px;overflow:hidden}
  body{
    background:var(--stage);
    font-family:"Open Sans",Arial,sans-serif;
    position:relative;
  }
  .rack-card{
    position:absolute;left:430px;top:18px;width:340px;height:766px;
    background:var(--paper);overflow:hidden;
    box-shadow:0 6px 20px rgba(0,0,0,.18);
  }
  .corner-shade{position:absolute;left:0;top:0;width:100%;height:100%}
  .brand{
    position:absolute;left:28px;top:38px;display:flex;align-items:center;gap:12px;
  }
  .brand-dot{width:58px;height:58px;border-radius:50%;background:var(--brand-blue)}
  .brand-name{font-weight:800;font-size:27px;color:var(--brand-blue);letter-spacing:.5px}
  .sky-fade{
    position:absolute;left:0;right:0;top:112px;height:110px;
    background:linear-gradient(#fff 0%,var(--sky-light) 60%,#9fc0e6 100%);
  }
  .headline{
    position:absolute;left:0;right:0;top:118px;text-align:center;
    font-weight:800;font-size:14.5px;letter-spacing:.2px;color:var(--ink-grey);
  }
  .headline .accent{color:var(--brand-blue)}
  .connector{
    position:absolute;left:0;right:0;top:140px;display:flex;justify-content:center;
    align-items:center;gap:14px;font-size:9px;font-weight:600;color:#fff;letter-spacing:.6px;
  }
  .connector::before,.connector::after{content:"";width:34px;height:1px;background:#fff}
  .service-banner{
    position:absolute;left:20px;top:158px;width:306px;height:34px;
    background:var(--brand-blue);transform:skewX(-8deg) rotate(-1.5deg);
    display:flex;align-items:center;justify-content:center;z-index:3;
  }
  .service-banner span{transform:skewX(8deg);color:#fff;font-weight:800;font-size:16.5px;letter-spacing:.3px}
  .home-photo{
    position:absolute;left:18px;right:0;top:210px;height:450px;
    background:linear-gradient(180deg,#9fc0e6 0%,#c3d5ea 20%,#7a6552 38%,#8b6f56 60%,#5e6a58 85%,#8a8f94 100%);
  }
  .contact-bar{
    position:absolute;left:0;right:0;bottom:0;height:70px;background:var(--footer-black);
    display:flex;align-items:flex-end;justify-content:center;gap:14px;padding-bottom:11px;
    color:#fff;font-weight:700;font-size:12px;z-index:3;
  }
  .contact-item{display:flex;align-items:center;gap:5px}
  .info-panel{
    position:absolute;left:44px;right:18px;top:430px;height:302px;
    background:var(--brand-blue);z-index:4;padding:58px 14px 0 12px;
  }
  .benefit{display:flex;gap:10px;margin-bottom:10px}
  .benefit-icon{flex:0 0 28px;height:28px;margin-top:20px}
  .benefit h3{color:#fff;font-size:10px;font-weight:800;letter-spacing:.3px;margin-bottom:3px}
  .benefit p{color:#fff;font-size:7.8px;line-height:1.35}
  .price-ribbon{
    position:absolute;left:18px;top:444px;width:196px;height:28px;
    background:var(--ribbon-red);transform:rotate(-20deg);z-index:5;
    display:flex;align-items:center;justify-content:center;
    color:#fff;font-weight:800;font-size:13px;letter-spacing:.5px;
  }
</style>
</head>
<body>
  <article class="rack-card">
    <svg class="corner-shade" viewBox="0 0 340 766" preserveAspectRatio="none" aria-hidden="true">
      <polygon points="0,0 118,0 30,40 0,120" fill="var(--paper-shade)"/>
      <polygon points="0,540 18,540 18,766 0,766" fill="var(--paper-shade)"/>
      <polygon points="300,600 340,585 340,766 300,766" fill="var(--paper-shade)"/>
    </svg>

    <div class="brand">
      <div class="brand-dot"></div>
      <div class="brand-name">HARBOR GROUP</div>
    </div>

    <div class="sky-fade"></div>
    <h1 class="headline">PROTECT YOUR <span class="accent">CLIENT'S GREATEST ASSET</span></h1>
    <div class="connector">WITH A</div>
    <div class="service-banner"><span>PRE-LISTING TERMITE INSPECTION</span></div>

    <div class="home-photo" role="img" aria-label="Photo of a two-storey brick family home with a double garage under a blue sky"></div>

    <footer class="contact-bar">
      <span class="contact-item">
        <svg width="14" height="14" viewBox="0 0 24 24" aria-hidden="true"><path d="M6.6 10.8a15 15 0 0 0 6.6 6.6l2.2-2.2a1 1 0 0 1 1-.25 11.4 11.4 0 0 0 3.6.57 1 1 0 0 1 1 1V20a1 1 0 0 1-1 1A17 17 0 0 1 3 4a1 1 0 0 1 1-1h3.5a1 1 0 0 1 1 1c0 1.25.2 2.45.57 3.6a1 1 0 0 1-.25 1z" fill="#fff"/></svg>
        1-800-555-0142
      </span>
      <span class="contact-item">
        <svg width="14" height="14" viewBox="0 0 24 24" aria-hidden="true"><circle cx="12" cy="12" r="9.5" fill="none" stroke="#fff" stroke-width="2"/><ellipse cx="12" cy="12" rx="4" ry="9.5" fill="none" stroke="#fff" stroke-width="1.6"/><path d="M3 12h18" stroke="#fff" stroke-width="1.6"/></svg>
        HarborInspect.com
      </span>
    </footer>

    <section class="info-panel">
      <div class="benefit">
        <svg class="benefit-icon" viewBox="0 0 28 28" aria-hidden="true"><circle cx="14" cy="14" r="11" fill="none" stroke="#fff" stroke-width="1.5"/><path d="M14 7v7l5 3" fill="none" stroke="#fff" stroke-width="1.5"/></svg>
        <div>
          <h3>SPEED UP THE SALES PROCESS</h3>
          <p>By having the seller conduct a termite inspection, you reduce the risk of delays or complications. With this essential step complete, you can expedite the transaction timeline and close deals faster!</p>
        </div>
      </div>
      <div class="benefit">
        <svg class="benefit-icon" viewBox="0 0 28 28" aria-hidden="true"><path d="M4 14 14 5l10 9v10H4z" fill="none" stroke="#fff" stroke-width="1.5"/><path d="M11 24v-6h6v6" fill="none" stroke="#fff" stroke-width="1.5"/></svg>
        <div>
          <h3>ENHANCE PROPERTY VALUE</h3>
          <p>Uncovering and remedying termite problems early can prevent costly damages and preserve the integrity of the home. With a clean bill of health from a termite inspection, you can market the property with confidence!</p>
        </div>
      </div>
      <div class="benefit">
        <svg class="benefit-icon" viewBox="0 0 28 28" aria-hidden="true"><rect x="4" y="4" width="20" height="20" rx="2" fill="none" stroke="#fff" stroke-width="1.5"/><path d="M9 14l4 4 7-8" fill="none" stroke="#fff" stroke-width="1.8"/></svg>
        <div>
          <h3>BOOST BUYER CONFIDENCE</h3>
          <p>A pre-listing termite inspection demonstrates proactive care for the property, instilling trust in potential buyers. Identifying issues upfront, you also eliminate surprises during negotiations, leading to smoother transactions and happier clients.</p>
        </div>
      </div>
    </section>

    <div class="price-ribbon">COMPETITIVE PRICES</div>
  </article>
</body>
</html>
```